Graphic design of trade booth

We have recently rebranded our logo and are looking for a redesign of our trade show booth. We have a template attached to show the dimensions.

The booth should have no other text on it except for our logo. We'd like for it to be stylized in a way that conforms to the new logo.

(Please note that our web site is not yet updated with the new logo so don't go there for inspiration.)

Attached: the new logo as well as the template for the booth layout.
Updates

All - please note that we may be switching our booth dimensions. We will have a final answer by tomorrow, March 20. In the event that we do switch, we will:

• post the new dimensions
• extend the competition
• add $$ to the award

Apologize for this, we are receiving some late-breaking information. Stay tuned and thanks for your interest. 

Hello Designers!

First of all, thank you very much for all your submission, and patience, as I know we have changed this project a little bit. Unfortunately, we need to make another change. We realize that many of you have invested time and energy into this project, and for that we truly apologize. In leu of this, we have added an additional $150 to this project - $100 additional for second place, and $50 additional for first place.

Here are the details for our new Banner project:
Please do not hesitate to let us know if you have any questions, etc... And again, we truly apologize for all the changes and updates to this project. Thanks for your participation! 

Target Market(s)

Scientists, executives in the life sciences information space. Rather boring and dull creatures who take themselves rather seriously.

Industry/Entity Type

Graphic Design

```html
<!DOCTYPE html>
<html lang="en">
<head>
<meta charset="utf-8">
<title>HelixSeeker Banner</title>
<link rel="stylesheet" href="https://fonts.googleapis.com/css2?family=Lexend:wght@600&display=swap">
<style>
  :root {
    --bg: #000000;
    --frame: #8a8a8a;
    --blue-deep: #3a00ff;
    --violet: #c400ff;
    --pink: #ff48ee;
    --cream: #f3e4b4;
    --brand: #1b8fc6;
  }
  html, body {
    margin: 0;
    padding: 0;
    width: 1200px;
    height: 460px;
    overflow: hidden;
    background: var(--bg);
  }
  .banner {
    position: relative;
    width: 1200px;
    height: 460px;
    background: var(--bg);
    box-sizing: border-box;
    border: 2px solid var(--frame);
    overflow: hidden;
  }
  .profile {
    position: absolute;
    top: 56px;
    height: 346px;
  }
  .profile--facing-right {
    border-radius: 120px 70px 10px 10px;
  }
  .profile--facing-left {
    border-radius: 70px 120px 10px 10px;
  }
  .profile--cool-a {
    left: 41px;
    width: 252px;
    background: linear-gradient(90deg, var(--blue-deep) 0%, var(--violet) 100%);
  }
  .profile--cool-b {
    left: 303px;
    width: 267px;
    background: linear-gradient(90deg, var(--violet) 0%, var(--blue-deep) 100%);
  }
  .profile--warm-a {
    left: 632px;
    width: 236px;
    background: linear-gradient(90deg, var(--pink) 0%, var(--cream) 100%);
  }
  .profile--warm-b {
    left: 878px;
    width: 282px;
    background: linear-gradient(90deg, var(--cream) 0%, var(--pink) 100%);
  }
  .brand {
    position: absolute;
    left: 84px;
    top: 116px;
    height: 158px;
    display: flex;
    align-items: center;
    gap: 30px;
  }
  .brand__dot {
    flex: none;
    width: 158px;
    height: 158px;
    border-radius: 50%;
    background: var(--brand);
  }
  .brand__name {
    font-family: "Lexend", sans-serif;
    font-weight: 600;
    font-size: 124px;
    line-height: 1;
    letter-spacing: 5px;
    color: var(--brand);
    white-space: nowrap;
    padding-top: 14px;
  }
</style>
</head>
<body>
  <main class="banner">
    <div class="profile profile--facing-right profile--cool-a" role="img" aria-label="Head silhouette in profile facing right, blue to violet gradient"></div>
    <div class="profile profile--facing-left profile--cool-b" role="img" aria-label="Head silhouette in profile facing left, violet to blue gradient"></div>
    <div class="profile profile--facing-right profile--warm-a" role="img" aria-label="Head silhouette in profile facing right, pink to cream gradient"></div>
    <div class="profile profile--facing-left profile--warm-b" role="img" aria-label="Head silhouette in profile facing left, cream to pink gradient"></div>
    <div class="brand">
      <span class="brand__dot" aria-hidden="true"></span>
      <span class="brand__name">HelixSeeker</span>
    </div>
  </main>
</body>
</html>
```